Wheels and Haulers OnOffer Price Sheet

Front and back marketing / Price Sheet hand-out. 5.5 x 8.5 Attached find images you can use and basic text data. We are looking for an innovated designer that can take this data and create an appealing hand-out that will be presented to car dealerships.
The related website is www.wheelsandhaulers.onoffer
Sleek, aggressive, impressive, appealing to an age range of 30+. Professional clientele suits.
We list car ads on our VELNO TV network and on our website. Our customers are national car / truck dealerships and individuals who want to sell a vehicle. This hand-out should advertise our company, our services and give them a look at our basic pricing.
Updates

We were so super pleased with the very first design that we boosted our budget up by 25%! You guys have talent!

Project Deadline Extended
Reason: we posted this over a USA holiday and think we can get more designs if we extend

Target Market(s)

Car and Truck Dealers across the USA

Industry/Entity Type

Marketing

Font styles to use
Serif
Sans Serif

Requirements
Must have
• Clarity in defining the price plans. The wire frame of the cars and the for sale sign as seen in the provided image.

```html
<!DOCTYPE html>
<html lang="en">
<head>
<meta charset="utf-8">
<title>Wheels and Haulers OnOffer – Price Sheet</title>
<link rel="stylesheet" href="https://fonts.googleapis.com/css2?family=Josefin+Sans:wght@300;600;700&family=Poiret+One&display=swap">
<style>
  :root {
    --bg-dark: #1f1f20;
    --bg-mid: #343436;
    --plan-purple: #5f2d8f;
    --plan-line: #4a2070;
    --face-top: #d4d3d8;
    --face-side: #9b9aa0;
    --accent-orange: #f26a21;
    --text-light: #e6e6e6;
    --text-grey: #cfcfd4;
    --marker-red: #e0262b;
    --white: #ffffff;
  }
  * { margin: 0; padding: 0; box-sizing: border-box; }
  html, body { width: 784px; height: 1200px; overflow: hidden; background: var(--bg-dark); }
  .sheet {
    position: relative;
    width: 784px; height: 1200px;
    overflow: hidden;
    background: radial-gradient(ellipse at 50% 40%, var(--bg-mid) 0%, #2a2a2b 55%, var(--bg-dark) 100%);
    font-family: "Josefin Sans", sans-serif;
    color: var(--text-light);
  }

  /* Header */
  .wire-art {
    position: absolute;
    background: linear-gradient(135deg, rgba(255,255,255,0.10), rgba(255,255,255,0.03));
    border-radius: 6px;
  }
  .wire-art.truck { left: 27px; top: 14px; width: 166px; height: 92px; }
  .wire-art.sportscar { left: 640px; top: 14px; width: 134px; height: 100px; }
  .brand {
    position: absolute; left: 200px; top: 40px; width: 432px;
    display: flex; align-items: center; justify-content: center; gap: 12px;
  }
  .brand-name {
    font-family: "Josefin Sans", sans-serif; font-weight: 600;
    font-size: 27px; line-height: 1; color: var(--white);
    padding-top: 4px; white-space: nowrap;
  }
  .brand-mark { width: 30px; height: 30px; background: var(--marker-red); flex: none; }

  /* Plans */
  .plan {
    position: absolute; left: 104px; width: 560px; height: 280px;
    background: var(--plan-purple);
    padding: 12px 26px 0 28px;
  }
  .plan::before {
    content: ""; position: absolute; left: 0; top: -13px; width: 100%; height: 13px;
    background: var(--face-top);
    transform: skewX(-45deg); transform-origin: bottom left;
  }
  .plan::after {
    content: ""; position: absolute; right: -13px; top: 0; width: 13px; height: 100%;
    background: var(--face-side);
    transform: skewY(-45deg); transform-origin: top left;
  }
  .plan.special { top: 134px; }
  .plan.dealer { top: 454px; }
  .plan.bonus { top: 778px; }

  .plan-name {
    display: inline-block;
    font-family: "Poiret One", sans-serif; font-weight: 400;
    font-size: 48px; line-height: 1.05; letter-spacing: 0.5px;
    color: var(--accent-orange);
    border-bottom: 2px solid var(--accent-orange);
    padding-right: 4px;
  }
  .price-row {
    display: flex; align-items: center; gap: 18px;
    margin-top: 4px; padding-bottom: 8px;
    border-bottom: 1px solid var(--plan-line);
  }
  .price {
    font-family: "Josefin Sans", sans-serif; font-weight: 700;
    font-size: 52px; color: var(--text-grey); line-height: 1; padding-top: 8px;
  }
  .network { font-weight: 700; font-size: 16px; line-height: 1.3; color: var(--text-light); }
  .network .channel {
    display: block; color: var(--accent-orange); font-size: 18px; font-weight: 700;
  }
  .specs { list-style: none; margin-top: 4px; }
  .specs li { font-weight: 700; font-size: 16px; line-height: 32px; color: var(--text-light); }
  .plan.bonus .specs { margin-top: 6px; }
  .plan.bonus .specs li { line-height: 23px; }
  .plan.bonus .price-row { padding-bottom: 6px; }

  /* Footer */
  .footer-note {
    position: absolute; left: 0; width: 100%; text-align: center;
    color: var(--text-grey); font-weight: 300;
  }
  .footer-note.addons { top: 1078px; font-size: 20px; }
  .footer-note.elite { top: 1112px; font-size: 14px; }
  .contact {
    position: absolute; left: 0; top: 1134px; width: 100%; text-align: center;
    font-family: "Josefin Sans", sans-serif; font-weight: 300;
    font-size: 38px; color: var(--white); letter-spacing: 0.5px;
  }
</style>
</head>
<body>
<main class="sheet">
  <header>
    <div class="wire-art truck" role="img" aria-label="White line drawing of a pickup truck seen from the rear"></div>
    <div class="brand">
      <h1 class="brand-name">Wheels and Haulers OnOffer</h1>
      <span class="brand-mark" aria-hidden="true"></span>
    </div>
    <div class="wire-art sportscar" role="img" aria-label="White line drawing of a sports car seen from the rear"></div>
  </header>

  <section class="plan special">
    <h2 class="plan-name">Special Deal</h2>
    <div class="price-row">
      <div class="price">$30</div>
      <p class="network"><span class="channel">VELNO TV</span>$1 a day / 1 ad for 30 days minumum</p>
    </div>
    <ul class="specs">
      <li>Max cars: 1</li>
      <li>Disk Storage: 30 MB</li>
      <li>Featured Cars: 0</li>
      <li>Account Life Time: 30 days</li>
    </ul>
  </section>

  <section class="plan dealer">
    <h2 class="plan-name">Dealer Package</h2>
    <div class="price-row">
      <div class="price">$810</div>
      <p class="network"><span class="channel">VELNO TV</span>90¢ a day / 10 ad for 90 days minumum</p>
    </div>
    <ul class="specs">
      <li>Max cars: 10</li>
      <li>Disk Storage: 200 MB</li>
      <li>Featured Cars: 0</li>
      <li>Account Life Time: 90 days</li>
    </ul>
  </section>

  <section class="plan bonus">
    <h2 class="plan-name">Bonus Dealer Package</h2>
    <div class="price-row">
      <div class="price">$810</div>
      <p class="network"><span class="channel">VELNO TV</span>90¢ a day / 10 ad for 90 days minumum<br>PLUS 3 featured vehicles on both<br>VELNO TV and the WEB</p>
    </div>
    <ul class="specs">
      <li>Max cars: 10</li>
      <li>Disk Storage: 200 MB</li>
      <li>Featured Cars: 3</li>
      <li>Account Life Time: 90 days</li>
    </ul>
  </section>

  <footer>
    <p class="footer-note addons">Featured packages may be bought as add-ons.</p>
    <p class="footer-note elite">If you want a larger package please call us we offer an execute package for the elite client.</p>
    <p class="contact">WheelsandHaulers.OnOffer 555-014-2290</p>
  </footer>
</main>
</body>
</html>
```